Business Card for Quillmark Ledger - A cannabis publication for executives.

I'd like some business cards for Quillmark Ledger. The logo is done (great job!) and I need a card design I will use with PRINTLY. I made it a short project to allow time for printing before an event. These will be standard sized cards (final artwork size 3.66" x 2.16" at 300dpi) with a final card size of 3.5" x 2.0". (See PRINTLY.com if you need more info.) I might try rounded corners but am not sure yet. I think the design will work okay with rounded.

Quillmark Ledger will be a bi-weekly publication for the cannabis industry. It is targeted to investors and industry executives, not consumers or pot smokers. So our market is more B2B. However I am open to creativity and making the card something people remark on.

My contact for card:

Dana Merrow
Founder/CEO
dana@quillmarkledger.example

2740 Harlow Avenue
Boston MA 02135
(617)555-0194

Target Market(s)

Executives, Industry people and investors in the Cannabis sector.

Contact Information for Business Card

PRINTLY does do double sided and the second side can be the same or different images. Only one side is required but use of the second side would be a bonus.

Font styles to use
Serif
Sans Serif
Decorative

Colors

Designer to choose colors to be used in the design.

Requirements
Must have
• Logo, contact info
Nice to have
• Style and design to make the card stand out in a crowd.

```html
<!DOCTYPE html>
<html lang="en">
<head>
<meta charset="utf-8">
<title>Quillmark Ledger — Business Card</title>
<link rel="stylesheet" href="https://fonts.googleapis.com/css2?family=Tinos:wght@400;700&display=swap">
<style>
  :root {
    --backdrop: #dcdedf;
    --card: #262626;
    --card-edge: #1c1c1c;
    --brand-blue: #1b74d1;
    --brand-green: #7cc22a;
    --name-cyan: #1aa6e2;
    --text-light: #f2f2f2;
  }
  * { box-sizing: border-box; margin: 0; padding: 0; }
  html, body {
    width: 1200px; height: 800px; overflow: hidden;
    background: var(--backdrop);
    font-family: "Tinos", "Times New Roman", serif;
  }
  .sheet {
    width: 1200px; height: 800px;
    display: flex; align-items: center; justify-content: center; gap: 48px;
  }
  .card {
    width: 532px; height: 304px;
    border-radius: 16px;
    background: linear-gradient(150deg, #2e2e2e 0%, var(--card) 55%, var(--card-edge) 100%);
    box-shadow: 0 10px 24px rgba(0,0,0,0.22);
    position: relative; overflow: hidden;
    color: var(--text-light);
  }

  /* Front */
  .card--front { display: flex; align-items: center; justify-content: center; }
  .wordmark { display: flex; align-items: center; gap: 14px; }
  .wordmark__dot { flex: none; border-radius: 50%; background: var(--brand-green); }
  .wordmark__name {
    color: var(--brand-blue); font-weight: 700; white-space: nowrap; letter-spacing: -0.5px;
  }
  .card--front .wordmark__dot { width: 40px; height: 40px; }
  .card--front .wordmark__name { font-size: 46px; }

  /* Back */
  .card--back .wordmark { position: absolute; left: 30px; top: 30px; gap: 9px; }
  .card--back .wordmark__dot { width: 22px; height: 22px; }
  .card--back .wordmark__name { font-size: 24px; }

  .contact {
    position: absolute; left: 30px; top: 84px;
    list-style: none; font-size: 14.5px; line-height: 1.25;
  }
  .contact__item { display: flex; align-items: flex-start; gap: 9px; margin-bottom: 7px; }
  .contact__icon {
    flex: none; width: 20px; height: 20px; border-radius: 50%;
    border: 1.5px solid var(--brand-green);
    display: flex; align-items: center; justify-content: center;
  }
  .contact__icon svg { width: 11px; height: 11px; }

  .divider {
    position: absolute; left: 296px; top: 60px; width: 2px; height: 190px;
    background: var(--brand-green);
  }
  .person {
    position: absolute; left: 318px; right: 30px; top: 150px;
    display: flex; align-items: flex-start; gap: 10px;
  }
  .person__badge {
    flex: none; width: 28px; height: 28px; border-radius: 50%;
    background: var(--brand-green); margin-top: 1px;
  }
  .person__name { color: var(--name-cyan); font-size: 25px; line-height: 1.05; white-space: nowrap; }
  .person__role { color: var(--brand-green); font-size: 14px; margin-top: 3px; }
</style>
</head>
<body>
<main class="sheet">

  <section class="card card--front" aria-label="Card front">
    <div class="wordmark">
      <span class="wordmark__dot"></span>
      <span class="wordmark__name">Quillmark Ledger</span>
    </div>
  </section>

  <section class="card card--back" aria-label="Card back">
    <div class="wordmark">
      <span class="wordmark__dot"></span>
      <span class="wordmark__name">Quillmark Ledger</span>
    </div>

    <ul class="contact">
      <li class="contact__item">
        <span class="contact__icon">
          <svg viewBox="0 0 12 12" fill="none" stroke="#7cc22a" stroke-width="1.4"><rect x="3" y="0.8" width="6" height="10.4" rx="1.2"/><line x1="5" y1="9.2" x2="7" y2="9.2"/></svg>
        </span>
        <span>(617)555-0194</span>
      </li>
      <li class="contact__item">
        <span class="contact__icon">
          <svg viewBox="0 0 12 12" fill="none" stroke="#7cc22a" stroke-width="1.3"><rect x="0.8" y="2.5" width="10.4" height="7" rx="0.8"/><polyline points="1,3 6,7 11,3"/></svg>
        </span>
        <span>dana@quillmarkledger.example</span>
      </li>
      <li class="contact__item">
        <span class="contact__icon">
          <svg viewBox="0 0 12 12" fill="none" stroke="#7cc22a" stroke-width="1.3"><polyline points="1,6 6,1.5 11,6"/><polyline points="2.5,5 2.5,10.5 9.5,10.5 9.5,5"/></svg>
        </span>
        <span>2740 Harlow Avenue<br>Boston MA 02135</span>
      </li>
    </ul>

    <div class="divider"></div>

    <div class="person">
      <span class="person__badge"></span>
      <div>
        <div class="person__name">Dana Merrow</div>
        <div class="person__role">Founder/CEO</div>
      </div>
    </div>
  </section>

</main>
</body>
</html>
```